Copperfield Hours - Podcast Cover

Copperfield Hours is a weekly podcast that dispels some of the myths about conventional economic thinking and provides a new way of thinking about issues that are faced by the global economy. It's insightful, thought-provoking and, most importantly, fun. We are refreshing the look and sound of the podcast. I have attached a copy of the old amateur design (which I did!)

Target Market(s)

Male oriented, smart folk with an interest in politics and economics

Font styles to use
Sans Serif

Requirements
Must have
• Clearly visible title, even when reduced in size. Must be 3000 pixels by 3000 pixels.
Nice to have
• This podcast challenges the status quo. It should reflect that. Photos and names of the hosts. Actually, because th ephotos are so different, we'd be open to the idea of a caricature if you can do that within the price.

```html
<!DOCTYPE html>
<html lang="en">
<head>
<meta charset="utf-8">
<title>The Copperfield Hours – Podcast Cover</title>
<link rel="stylesheet" href="https://fonts.googleapis.com/css2?family=Open+Sans:wdth,wght@75..100,700..800&family=Sorts+Mill+Goudy&display=swap">
<style>
  :root {
    --navy-deep: #0b1430;
    --navy: #15214a;
    --navy-mid: #1d2b58;
    --gold-light: #fdf1c9;
    --gold: #eccb7f;
    --frame: #a9a77c;
    --band-blue: #15287a;
    --band-edge: #0d1a55;
    --cream: #f6e8c2;
  }
  * { margin: 0; padding: 0; box-sizing: border-box; }
  html, body { width: 1200px; height: 1200px; overflow: hidden; background: var(--navy-deep); }
  .cover {
    position: relative;
    width: 1200px;
    height: 1200px;
    overflow: hidden;
    background:
      radial-gradient(ellipse 70% 55% at 50% 45%, var(--navy-mid) 0%, var(--navy) 45%, var(--navy-deep) 100%);
  }
  .market-backdrop {
    position: absolute;
    inset: 0;
    background:
      linear-gradient(180deg, rgba(255,255,255,0.03) 0%, rgba(255,255,255,0) 60%),
      radial-gradient(ellipse 30% 20% at 20% 25%, rgba(120,140,190,0.10), transparent 70%),
      radial-gradient(ellipse 25% 25% at 85% 30%, rgba(120,140,190,0.08), transparent 70%);
  }
  .artwork { position: absolute; inset: 0; width: 1200px; height: 1200px; }
  .host-photo, .centre-photo { position: absolute; }
  .host-photo--left {
    left: 0; top: 646px; width: 460px; height: 444px;
    background: radial-gradient(ellipse 60% 70% at 45% 70%, #2c8c98 0%, #1f6b78 55%, rgba(21,33,74,0) 100%);
  }
  .host-photo--right {
    left: 820px; top: 636px; width: 380px; height: 454px;
    background: radial-gradient(ellipse 60% 70% at 50% 75%, #e6e6e2 0%, #b9b8b3 50%, rgba(21,33,74,0) 100%);
  }
  .centre-photo {
    left: 456px; top: 677px; width: 352px; height: 379px;
    background: radial-gradient(circle at 50% 60%, #a7b79a 0%, #6f8468 50%, rgba(21,33,74,0) 80%);
  }
  .host-band {
    position: absolute;
    left: 0; top: 1090px; width: 1200px; height: 72px;
    background: linear-gradient(180deg, var(--band-blue) 0%, var(--band-edge) 100%);
    display: flex; align-items: center; justify-content: center;
  }
  .host-names {
    font-family: "Sorts Mill Goudy", "Goudy Old Style", serif;
    font-size: 44px;
    color: var(--cream);
    letter-spacing: 0.5px;
    line-height: 1;
  }
  .footer-strip {
    position: absolute; left: 0; top: 1162px; width: 1200px; height: 38px;
    background: var(--navy-deep);
  }
</style>
</head>
<body>
<main class="cover">
  <div class="market-backdrop"></div>

  <svg class="artwork" viewBox="0 0 1200 1200" xmlns="http://www.w3.org/2000/svg" aria-hidden="true">
    <defs>
      <linearGradient id="goldText" x1="0" y1="0" x2="0" y2="1">
        <stop offset="0" stop-color="#fff4d0"/>
        <stop offset="1" stop-color="#e8c574"/>
      </linearGradient>
      <linearGradient id="goldIcon" x1="0" y1="0" x2="0" y2="1">
        <stop offset="0" stop-color="#f6dc92"/>
        <stop offset="1" stop-color="#d9a93f"/>
      </linearGradient>
      <filter id="titleShadow" x="-10%" y="-10%" width="120%" height="130%">
        <feDropShadow dx="4" dy="6" stdDeviation="5" flood-color="#000" flood-opacity="0.55"/>
      </filter>
    </defs>

    <!-- frame -->
    <g class="frame" fill="none" stroke="var(--frame)" stroke-width="1.5">
      <polyline points="494,56 65,56 65,578 92,578"/>
      <polyline points="699,56 1140,56 1140,578 1112,578"/>
    </g>

    <!-- microphone icon -->
    <g class="mic-icon" fill="none" stroke="url(#goldIcon)" stroke-width="5" stroke-linecap="round">
      <rect x="581" y="42" width="38" height="64" rx="19"/>
      <line x1="590" y1="60" x2="610" y2="60"/>
      <line x1="590" y1="70" x2="610" y2="70"/>
      <line x1="590" y1="80" x2="610" y2="80"/>
      <line x1="590" y1="90" x2="610" y2="90"/>
      <path d="M568 82 v6 a32 32 0 0 0 64 0 v-6"/>
      <line x1="600" y1="120" x2="600" y2="140"/>
      <line x1="588" y1="142" x2="612" y2="142"/>
    </g>

    <!-- title -->
    <g class="title" fill="url(#goldText)" filter="url(#titleShadow)"
       font-family="'Open Sans', Arial, sans-serif" font-weight="800" style="font-stretch:75%" text-anchor="middle">
      <text x="600" y="304" font-size="200" textLength="286" lengthAdjust="spacingAndGlyphs">THE</text>
      <text x="602" y="472" font-size="205" textLength="1020" lengthAdjust="spacingAndGlyphs">COPPERFIELD</text>
      <text x="602" y="637" font-size="205" textLength="600" lengthAdjust="spacingAndGlyphs">HOURS</text>
    </g>
  </svg>

  <div class="host-photo host-photo--left" role="img" aria-label="Portrait photo of the first host, smiling, wearing a teal polo shirt"></div>
  <div class="centre-photo" role="img" aria-label="Photo of a bomb made of wrapped banknotes with a lit fuse"></div>
  <div class="host-photo host-photo--right" role="img" aria-label="Portrait photo of the second host, wearing glasses and a white printed t-shirt"></div>

  <div class="host-band">
    <p class="host-names">Milesharrow &amp; ProfAlanReeve</p>
  </div>
  <div class="footer-strip"></div>
</main>
</body>
</html>
```